Business card - mobile service

O KiraTel is a mobile family safety service based on tablets and smartphones.
The business card must have:
BASIC INFO
Company Logo
Name
Position / Job Title: Co-founder
Mobile Phone Number: +55 (11) 5080 6172
Land Line: +55 (11) 9087 614352
Email Address: name@kiratel-example.com
Web Site URL: www.kiratel-example.com
PROMOTIONAL INFO
Try KiraTel free Today!
Your personal promo code: xxxx-2222-uuuu-7777-1234
Promo code text explanation with the instructions about the trial offer
Updates
Dears,
One more must have: the KiraTel slogan:
Industry/Entity Type
Safety
Look and feel
Each slider illustrates characteristics of the customer's brand and the style your logo design should communicate.

```html
<!DOCTYPE html>
<html lang="en">
<head>
<meta charset="utf-8">
<title>KiraTel Business Card</title>
<link href="https://fonts.googleapis.com/css2?family=Ubuntu:wght@400;500;700&display=swap" rel="stylesheet">
<style>
  :root {
    --bg: #e4e4e4;
    --yellow: #ffc845;
    --yellow-pale: #ffdb85;
    --blue: #2ea8e0;
    --white: #ffffff;
    --ink: #2b2b2b;
  }
  * { box-sizing: border-box; margin: 0; padding: 0; }
  html, body { width: 1200px; height: 900px; overflow: hidden; }
  body {
    background: var(--bg);
    font-family: "Ubuntu", Arial, sans-serif;
    position: relative;
  }
  .card {
    position: absolute;
    width: 500px;
    height: 288px;
    overflow: hidden;
    box-shadow: 0 4px 10px rgba(0,0,0,0.18);
  }

  /* Front */
  .card-front { left: 80px; top: 204px; background: var(--yellow); }
  .front-pale-strip {
    position: absolute; left: 44px; top: 0; width: 10px; height: 100%;
    background: var(--yellow-pale);
  }
  .front-panel {
    position: absolute; left: 54px; top: 0; width: 146px; height: 278px;
    background: var(--white);
  }
  .front-panel-bar {
    position: absolute; left: 54px; top: 278px; width: 146px; height: 10px;
    background: var(--blue);
  }
  .brand {
    position: absolute; display: flex; align-items: center; gap: 6px;
    font-weight: 700; color: var(--blue); letter-spacing: -0.5px;
  }
  .front-brand { left: 66px; top: 40px; font-size: 30px; }
  .brand-dot {
    width: 14px; height: 14px; border-radius: 50%; background: var(--yellow);
    flex: none;
  }
  .front-slogan {
    position: absolute; left: 54px; top: 204px; width: 146px;
    text-align: center; color: var(--blue); font-size: 13px; line-height: 17px;
  }
  .contact {
    position: absolute; left: 280px; top: 76px; color: var(--ink);
  }
  .contact-name { color: var(--blue); font-weight: 700; font-size: 19px; }
  .contact-role { font-size: 12px; margin-top: 4px; }
  .contact-list { list-style: none; margin-top: 32px; font-size: 12px; line-height: 20px; }
  .contact-list b { color: var(--blue); font-weight: 700; margin-right: 4px; }
  .contact-web { font-size: 12px; margin-top: 14px; }

  /* Back */
  .card-back { left: 620px; top: 404px; background: var(--blue); height: 286px; }
  .back-band {
    position: absolute; left: 0; top: 72px; width: 476px; height: 134px;
    background: var(--white);
  }
  .back-tab {
    position: absolute; left: 476px; top: 72px; width: 24px; height: 134px;
    background: var(--yellow);
  }
  .promo {
    position: absolute; right: 216px; top: 90px; text-align: right; color: var(--ink);
    font-size: 12px; line-height: 16px;
  }
  .promo-title { color: var(--blue); font-weight: 700; font-size: 17px; margin-bottom: 8px; }
  .back-brand { left: 308px; top: 120px; font-size: 32px; }
  .back-slogan {
    position: absolute; left: 0; width: 476px; top: 230px; text-align: center;
    color: var(--white); font-size: 15px; font-weight: 500;
  }
</style>
</head>
<body>
  <section class="card card-front">
    <div class="front-pale-strip"></div>
    <div class="front-panel"></div>
    <div class="front-panel-bar"></div>
    <div class="brand front-brand"><span>KiraTel</span><span class="brand-dot"></span></div>
    <p class="front-slogan">Your Family<br>Safety Service</p>
    <div class="contact">
      <h1 class="contact-name">Lena Ortiz</h1>
      <p class="contact-role">Co-founder</p>
      <ul class="contact-list">
        <li><b>M</b>+55 (11) 5080 6172</li>
        <li><b>T</b>+55 (11) 9087 614352</li>
        <li><b>E</b>name@kiratel-example.com</li>
      </ul>
      <p class="contact-web">www.kiratel-example.com</p>
    </div>
  </section>

  <section class="card card-back">
    <div class="back-band"></div>
    <div class="back-tab"></div>
    <div class="promo">
      <h2 class="promo-title">Try KiraTel free Today!</h2>
      <p>Your personal promo code:</p>
      <p>xxxx-2222-uuuu-7777-1234</p>
      <p>Promo code text explanation with</p>
      <p>the instructions about the trial offer.</p>
    </div>
    <div class="brand back-brand"><span>KiraTel</span><span class="brand-dot"></span></div>
    <p class="back-slogan">Your Family Safety Service</p>
  </section>
</body>
</html>
```